VELOXA SPORTS NETWORK

design a website that will be a companion to a sports network that features womens sports and fitness content.
With the goal of promoting and empowering female athleticism, Veloxatv.example will be the online network that connects female sports fans to the sports they love and follow. The site aims to raise the level of awareness of women in sports by providing comprehensive sports coverage, spotlighting outstanding achievements, and working with sporting associations on advocacy issues and empowering programs.
Updates
I would like to have all entry by Sunday June 8 2014 thank you
please use actual script not lorem ipsum
thank you
Deadline winding down, added new pictures to file
Target Market(s)
our target market is females 18-54, whom love womens sports and ftiness
Industry/Entity Type
Fitness
Requirements
Must have
- Attributes of the website:
1. Large Photos: to accompany current stories
2. Colorful: Highlight Veloxa’s officials colors
3. News Area: recent news items on the home page and achieved news stories
4. Featured Content area: Headline news, athlete spotlights and issues
5. Streaming content: to accompany news and featured content
6. Advertiser links: to purchase merchandise
7. Real-time scores of live events
8. Blog
9. Monthly newsletter
10. Athlete profile page
11. Model close to QRVT
Nice to have
- Veloxatv.example will offer value-added service that will entitle customers to gain access to online streaming services provided by Veloxa, which delivers both live streams and on-demand replays of global women’s sports events to sports fans in U.S. and abroad. This service will be subscription based for a modest monthly fee. Content will be available across multiple platforms and cloud based. New subscriber will get first 30 days free.
Content will include:
1. Live sports events
2. On-demand and premium content
3. Fan-generated Content

```html
<!DOCTYPE html>
<html lang="en">
<head>
<meta charset="utf-8">
<title>Veloxa Sports Network</title>
<link href="https://fonts.googleapis.com/css2?family=Varela+Round&family=Open+Sans:wght@400;600&display=swap" rel="stylesheet">
<style>
:root{
  --orange:#e8542d;
  --orange-light:#f27a45;
  --orange-dark:#d3391b;
  --yellow:#f5b20c;
  --ink:#2a2a2a;
  --body:#666;
  --muted:#888;
  --line:#dedede;
  --footer:#1c1c1c;
  --white:#fff;
}
*{margin:0;padding:0;box-sizing:border-box}
html,body{width:1200px;height:2368px;overflow:hidden;background:var(--white)}
body{position:relative;font-family:"Open Sans",Arial,sans-serif;color:var(--body);font-size:12px;line-height:1.6}
.abs{position:absolute}
h1,h2,h3,h4,.display{font-family:"Varela Round","Open Sans",sans-serif;font-weight:400}

/* hero */
.hero{left:0;top:0;width:1200px;height:627px;background:linear-gradient(180deg,#c9c2d4 0%,#8c7f8e 25%,#5a4a4c 45%,#3f7a2e 60%,#4f9a34 80%,#3c6d2a 100%)}
.logo{left:120px;top:26px;display:flex;align-items:center;gap:14px;color:var(--orange)}
.logo-mark{width:62px;height:62px;border-radius:50%;background:var(--orange)}
.logo-name{font-family:"Varela Round",sans-serif;font-size:40px;line-height:1;letter-spacing:2px}
.logo-sub{font-family:"Varela Round",sans-serif;font-size:14px;letter-spacing:1px;margin-top:4px}
.nav{left:95px;top:103px;width:1005px;height:52px;background:linear-gradient(180deg,var(--orange-light),var(--orange-dark));clip-path:polygon(2% 0,100% 0,98% 100%,0 100%);display:flex;justify-content:flex-end;padding-right:30px}
.nav a{color:var(--white);text-decoration:none;font-family:"Varela Round",sans-serif;font-size:17px;line-height:52px;padding:0 24px;border-left:1px solid rgba(255,255,255,.35);transform:skewX(-20deg)}
.nav a span{display:inline-block;transform:skewX(20deg)}
.nav a:first-child{border-left:none}
.hero-title{left:0;top:335px;width:1200px;text-align:center;color:var(--white);text-shadow:0 2px 6px rgba(0,0,0,.55)}
.hero-title h1{font-size:42px;letter-spacing:1px;line-height:1.2}
.hero-title h2{font-size:28px;letter-spacing:1px;line-height:1.3}
.hero-arrow{top:300px}
.dots{left:565px;top:596px;display:flex;gap:6px}
.dots i{width:13px;height:13px;border-radius:50%;background:var(--white);display:block}

/* feature strip */
.features{left:110px;top:628px;width:980px;height:256px;background:var(--white);border:1px solid #eee;box-shadow:0 0 40px rgba(0,0,0,.06)}
.tile{top:24px;width:285px;height:199px}
.tile .photo{height:132px}
.tile .caption{height:67px;padding:10px 18px;color:var(--white)}
.tile h3{font-size:20px;line-height:1.2}
.tile p{font-size:11px;opacity:.9}
.tile svg{position:absolute;right:14px;bottom:18px}
.scores{left:620px;top:24px;width:339px;height:199px;border:1px solid var(--line)}
.scores h3{font-size:18px;color:var(--ink);padding:12px 18px;background:linear-gradient(#fafafa,#ededed);border-bottom:1px solid var(--line)}
.scores table{width:300px;margin:6px 0 0 18px;border-collapse:collapse;font-size:12px}
.scores td{padding:3px 0;border-bottom:1px solid #eee;color:var(--ink)}
.scores td:first-child{color:var(--orange)}
.scores td:first-child::before{content:"";display:inline-block;border:4px solid transparent;border-left-color:var(--orange);margin-right:6px}

/* main column */
.main{left:107px;width:620px}
.welcome h2{font-size:25px;color:var(--orange);margin-bottom:8px}
.welcome p{font-size:12px;margin-bottom:10px;line-height:1.65}
.section-title{font-size:22px;color:var(--ink);margin-bottom:14px}
.event{width:300px;height:80px;display:flex;gap:12px}
.event .photo{width:124px;height:78px;flex:none}
.event h4{font-size:16px;color:var(--orange);line-height:1.3}
.event p{font-size:11.5px;line-height:1.6}
.news{width:300px}
.news h4{font-size:16px;color:var(--ink);line-height:1.4;font-family:"Open Sans",sans-serif}
.news p{font-size:11.5px;line-height:1.6}
.news .date{margin-top:4px}

/* sidebar */
.side{left:756px;width:314px}
.blog{top:916px;height:360px;border:1px solid var(--line);overflow:hidden}
.blog h3{background:linear-gradient(#3a3a3a,#1a1a1a);color:var(--white);font-size:22px;padding:10px 24px;height:52px}
.post{display:flex;gap:14px;padding:0 20px 0 24px;height:88px;margin-top:12px}
.post:first-of-type{margin-top:20px}
.post .photo{width:72px;height:64px;flex:none;margin-top:4px}
.post h4{font-size:13px;line-height:1.5;color:var(--orange);font-family:"Open Sans",sans-serif}
.post p{font-size:10.5px;line-height:1.6;color:var(--muted);white-space:nowrap}
.post .date{color:var(--body)}
.newsletter{top:1290px;height:152px;background:linear-gradient(var(--orange-light),var(--orange-dark));color:var(--white);padding:18px 26px}
.newsletter h3{font-size:25px;line-height:1.2}
.newsletter p{font-size:11.5px;line-height:1.5;margin:6px 0 10px}
.btn{display:inline-block;background:var(--orange);color:var(--white);font-family:"Varela Round",sans-serif;border-radius:3px}
.newsletter .btn{background:#f58a2c;font-size:15px;padding:6px 26px}
.ads{top:1456px;height:222px;border:1px solid var(--line)}
.ads h3{font-size:20px;color:var(--ink);padding:14px 24px;background:linear-gradient(#fafafa,#ececec);border-bottom:1px solid var(--line)}
.ads ul{list-style:none;padding:10px 30px}
.ads li{font-size:12px;color:var(--ink);line-height:29px}
.ads li::before{content:"›";color:var(--muted);margin-right:12px}

/* content row */
.promo{top:1745px;width:480px}
.promo h3{font-size:20px;color:var(--orange);margin-bottom:12px}
.promo .photo{position:absolute;left:2px;top:38px;width:158px;height:150px}
.promo .text{position:absolute;left:176px;top:36px;width:300px}
.promo h4{font-size:16px;color:var(--ink);font-family:"Open Sans",sans-serif;margin-bottom:4px}
.promo p{font-size:11.5px;line-height:1.65}
.promo .btn{margin-top:10px;font-size:13px;padding:6px 20px;background:linear-gradient(#f06a40,var(--orange-dark))}

/* footer */
.footer{left:0;top:2008px;width:1200px;height:360px;background:var(--footer);border-top:9px solid var(--orange)}
.fcol{top:62px}
.fcol h4{font-size:19px;color:var(--white);margin-bottom:12px}
.fcol li{list-style:none;font-size:12.5px;color:#ddd;line-height:24px;padding-left:3px}
.footer-bottom{left:0;top:2296px;width:1200px;border-top:1px solid #333;padding:24px 0 0 116px;font-size:12px;color:#bbb}
</style>
</head>
<body>

<section class="hero abs" role="img" aria-label="Floodlit football stadium at dusk seen from the upper stand"></section>
<div class="logo abs">
  <div class="logo-mark"></div>
  <div><div class="logo-name">VELOXA</div><div class="logo-sub">SPORTS NETWORK</div></div>
</div>
<nav class="nav abs">
  <a><span>ABOUT</span></a><a><span>GAMES</span></a><a><span>NEWS</span></a><a><span>BLOG</span></a><a><span>EVENTS</span></a><a><span>SERVICES</span></a><a><span>SUPPORT</span></a><a><span>CONTACT</span></a>
</nav>
<div class="hero-title abs">
  <h1>NULLA RHONCUS DICTUM CURABITUR</h1>
  <h2>VESTIBULUM LIGULA AUGUE BIBEND</h2>
</div>
<svg class="hero-arrow abs" style="left:50px" width="40" height="110" viewBox="0 0 40 110"><polyline points="36,2 4,55 36,108" fill="none" stroke="#fff" stroke-width="2"/></svg>
<svg class="hero-arrow abs" style="left:1108px" width="40" height="110" viewBox="0 0 40 110"><polyline points="4,2 36,55 4,108" fill="none" stroke="#fff" stroke-width="2"/></svg>
<div class="dots abs"><i></i><i></i><i></i><i></i></div>

<section class="features abs">
  <div class="tile abs" style="left:27px">
    <div class="photo" role="img" aria-label="Basketball players on court" style="background:linear-gradient(135deg,#3b4f7a,#b98a68,#2d3a5a)"></div>
    <div class="caption" style="background:var(--orange-light)">
      <h3>LATEST STORIES</h3><p>Nulla sit amet diam Duis non nunc liber</p>
    </div>
    <svg width="14" height="32" viewBox="0 0 14 32"><polyline points="2,2 12,16 2,30" fill="none" stroke="#fff" stroke-width="2"/></svg>
  </div>
  <div class="tile abs" style="left:324px">
    <div class="photo" role="img" aria-label="Football players contesting the ball" style="background:linear-gradient(135deg,#6b3a3a,#b03030,#4a7a3a)"></div>
    <div class="caption" style="background:var(--yellow)">
      <h3>FEATURED NEWS</h3><p>Nulla sit amet diam Duis non nunc liber</p>
    </div>
    <svg width="14" height="32" viewBox="0 0 14 32"><polyline points="2,2 12,16 2,30" fill="none" stroke="#fff" stroke-width="2"/></svg>
  </div>
  <div class="scores abs">
    <h3>REAL-TIME SCORES</h3>
    <table>
      <tr><td>Phasellus felis</td><td>0223</td><td>First</td></tr>
      <tr><td>Dolor scelerisque</td><td>256</td><td>Second</td></tr>
      <tr><td>Yempus eget</td><td>396</td><td>Thrid</td></tr>
      <tr><td>Lobortis libero</td><td>456</td><td>Fourth</td></tr>
      <tr><td>Aliquam nec erat</td><td>596</td><td>Fifth</td></tr>
    </table>
  </div>
</section>

<section class="main welcome abs" style="top:925px">
  <h2>Welcome to Veloxa Sports Network</h2>
  <p>Veloxatv.example will offer value-added service that will entitle customers to gain access to online streaming services provided by Veloxa, which delivers both live streams and on-demand replays of global women's sports events to sports fans in U.S. and abroad. This service will be subscription based for a modest monthly fee.</p>
  <p>Content will be available across multiple platforms and cloud based. New subscriber will get first 30 days free.</p>
</section>

<section class="main abs" style="top:1088px;height:270px">
  <h3 class="section-title">LIVE SPORTS EVENTS</h3>
  <div class="event abs" style="left:3px;top:44px"><div class="photo" role="img" aria-label="Cheering team group" style="background:linear-gradient(135deg,#4a6aa0,#e0d0c0)"></div><div><h4>Event Tittle here</h4><p>Phasellus felis dolor scelerisque a tempus eget lobortis id libero Aliqu</p></div></div>
  <div class="event abs" style="left:317px;top:44px"><div class="photo" role="img" aria-label="Football player under blue sky" style="background:linear-gradient(135deg,#6fa0d8,#e8eef5)"></div><div><h4>Event Tittle here</h4><p>Phasellus felis dolor scelerisque a tempus eget lobortis id libero Aliqu</p></div></div>
  <div class="event abs" style="left:3px;top:157px"><div class="photo" role="img" aria-label="Team lined up on a pitch" style="background:linear-gradient(135deg,#4e9a3a,#a0c070)"></div><div><h4>Event Tittle here</h4><p>Phasellus felis dolor scelerisque a tempus eget lobortis id libero Aliqu</p></div></div>
  <div class="event abs" style="left:317px;top:157px"><div class="photo" role="img" aria-label="Player leaping over a crowd" style="background:linear-gradient(180deg,#eae6e0,#a07050)"></div><div><h4>Event Tittle here</h4><p>Phasellus felis dolor scelerisque a tempus eget lobortis id libero Aliqu</p></div></div>
</section>

<section class="main abs" style="top:1368px;height:320px">
  <h3 class="section-title">LATEST NEWS</h3>
  <div class="news abs" style="left:0;top:44px"><h4>Mauris vel lacus vitae felis</h4><p>Pellentesque faucibus Ut accumsan ultricies Maecenas</p><p class="date">Posted on 28 Feb 2014</p></div>
  <div class="news abs" style="left:325px;top:44px"><h4>Duis non nunc Nulla rhoncu</h4><p>Pellentesque faucibus Ut accumsan ultricies Maecenas</p><p class="date">Posted on 28 Feb 2014</p></div>
  <div class="news abs" style="left:0;top:136px"><h4>Morbi porta libero id ullamcorper</h4><p>Pellentesque faucibus Ut accumsan ultricies Maecenas</p><p class="date">Posted on 28 Feb 2014</p></div>
  <div class="news abs" style="left:325px;top:136px"><h4>Donec convallis pede venenatis</h4><p>Pellentesque faucibus Ut accumsan ultricies Maecenas</p><p class="date">Posted on 28 Feb 2014</p></div>
  <div class="news abs" style="left:0;top:224px"><h4>Nam eget lacus Aliquam</h4><p>Etiam est nunc venenatis in tristique eu imperdiet ac nisl Cum sociis natoque penatibus</p><p class="date">Posted on 28 Feb 2014</p></div>
  <div class="news abs" style="left:325px;top:224px"><h4>Praesent elementum</h4><p>Etiam est nunc venenatis in tristique eu imperdiet ac nisl Cum sociis natoque penatibus</p><p class="date">Posted on 28 Feb 2014</p></div>
</section>

<aside class="side blog abs">
  <h3>Recent Blog Post</h3>
  <div class="post"><div class="photo" role="img" aria-label="Football match action" style="background:linear-gradient(135deg,#2f8a3a,#d0e0c0)"></div><div><h4>Nulla sit amet</h4><p>Maecenas at justo id velit placerat<br>molestie Donec dictum lectus</p><p class="date">Posted 2 hours ago</p></div></div>
  <div class="post"><div class="photo" role="img" aria-label="Players on a pitch" style="background:linear-gradient(135deg,#4a9a3a,#c04040)"></div><div><h4>Nulla sit amet</h4><p>Maecenas at justo id velit placerat<br>molestie Donec dictum lectus</p><p class="date">Posted 2 hours ago</p></div></div>
  <div class="post"><div class="photo" role="img" aria-label="Footballer with ball" style="background:linear-gradient(135deg,#3a5a3a,#a03030)"></div><div><h4>Nulla sit amet</h4><p>Maecenas at justo id velit placerat<br>molestie Donec dictum lectus</p><p class="date">Posted 2 hours ago</p></div></div>
</aside>
<aside class="side newsletter abs">
  <h3>Monthly Newsletters</h3>
  <p>Curabitur tristique mi condimentum orci Phasellus pellentesque aliquam enim</p>
  <span class="btn">SUBSCRIBE</span>
</aside>
<aside class="side ads abs">
  <h3>Advertise Links</h3>
  <ul><li>Pellentesque faucibus accumsan</li><li>Altricies elit Maecenas</li><li>Velit placerat molestie</li><li>Donec dictum lectus</li><li>Non odio Cras</li></ul>
</aside>

<section class="promo abs" style="left:109px;height:200px">
  <h3>On-demand and premium content</h3>
  <div class="photo" role="img" aria-label="American football helmet close-up" style="background:linear-gradient(135deg,#b02020,#e05040,#3a6a2a)"></div>
  <div class="text"><h4>Phasellus felis dolor scelerisque</h4><p>a tempus eget lobortis id libero Aliquam nec erat at purus cursus interdum Vestibulum ligula augue bibendum accumsan vestibulum ut commodo a mi Morbi ornare gravida elit Integer congue Augue et malesuada iaculis ipsum dui aliquet felis</p><span class="btn">READ MORE</span></div>
</section>
<section class="promo abs" style="left:612px;height:200px">
  <h3>Fan-generated Content</h3>
  <div class="photo" role="img" aria-label="Group of cheering fans" style="background:linear-gradient(135deg,#e8e0d8,#a08878)"></div>
  <div class="text"><h4>Phasellus felis dolor scelerisque</h4><p>a tempus eget lobortis id libero Aliquam nec erat at purus cursus interdum Vestibulum ligula augue bibendum accumsan vestibulum ut commodo a mi Morbi ornare gravida elit Integer congue Augue et malesuada iaculis ipsum dui aliquet felis</p><span class="btn">READ MORE</span></div>
</section>

<footer class="footer abs">
  <div class="fcol abs" style="left:126px"><h4>COMPANY</h4><ul><li>HOME</li><li>ABOUT US</li><li>UPCOMIN GAME</li><li>PHOTOS</li><li>CONTACT US</li></ul></div>
  <div class="fcol abs" style="left:298px"><h4>FEATURED GAME</h4><ul><li>ALIQUAM NEC</li><li>ERAT AT PURUS CURSUS</li><li>INTERDUM VESTI</li><li>BULUM LIGULA</li><li>AUGUE BIBEND</li></ul></div>
  <div class="fcol abs" style="left:510px"><h4>SUPPORT</h4><ul><li>BEST PLAYERS</li><li>TEAMS</li><li>AWARDS</li><li>VIDEOS</li><li>PHOTOS</li></ul></div>
  <div class="fcol abs" style="left:687px"><h4>SUBLINKS</h4><ul><li>ALIQUAM</li><li>PURUS CURSUS</li><li>INTERDUM VESTI</li><li>BULUM LI</li><li>AUGUE BIBEND</li></ul></div>
  <div class="fcol abs" style="left:892px"><h4>SUBLINKS</h4><ul><li>SUPPORT</li><li>FAQ</li><li>TESTIMONIALS</li><li>RECENT BLOG</li><li>CONTACT</li></ul></div>
</footer>
<div class="footer-bottom abs">© 2014 Company Name.&nbsp; All right reserved.&nbsp; Term of Use</div>

</body>
</html>
```